Website for new academic journal of deconstruction and psychoanalysis

- This project has been put on hold because of a mistake I made. I requested that the project be for a journal cover and matching website. The problem was that I was trying to get web designers to design a book cover first, and it was not working. I have started a new project for a book or journal cover. Once that project has been completed, I will bring the book cover design over to this project so that it can be used with the website design. This way this design project can focus on the function of the website. -

The function of the website will be similar to the function of these other KRB journals. I give you these other journals just as examples of journal websites and journal covers:

http://www.qvrm.dalbrook.ac.uk/
http://archive.fenwold.edu/
http://www.gmt.halvercrest.edu/~vostrine/
http://www.tamberlyreview.org/subscribe/subscribe-to-tamberly/

The MV website will have the following buttons/pages:

Home
About the Journal
Issues
News and Events
Blog
Submissions
Contact
Links
Updates

- This project has been put on hold because of a mistake I made.  I requested that the project be for a journal cover and matching website.  The problem was that I was trying to get web designers to design a book cover first, and it was not working.  I have started a new project for a book or journal cover.  Once that project has been completed, I will bring the book cover design over to this project so that it can be used with the website design.  This way this design project can focus on the function of the website. -

Target Market(s)

Professional academics and psychoanalytic clinicians.

Industry/Entity Type

Events

Font styles to use
Sans Serif

Requirements
Nice to have
• A very contemporary feel. Simplicity. Bold colors.
Should not have
• NO photos of Hallam or Lemoyne, or photos of anyone. No photos of books or academic icons.

```html
<!DOCTYPE html>
<html lang="en">
<head>
<meta charset="utf-8">
<title>The Mutable Veil – Studies in Deconstruction and Psychoanalysis</title>
<link rel="stylesheet" href="https://fonts.googleapis.com/css2?family=Arimo:wght@400;700&display=swap">
<style>
  :root {
    --page-bg: #ffffff;
    --frame-bg: #efefef;
    --brand-blue: #0a4f9c;
    --brand-blue-deep: #063a78;
    --nav-top: #5a5a5a;
    --nav-bottom: #393939;
    --nav-divider: #6a6a6a;
    --panel-bg: #ffffff;
    --panel-border: #dddddd;
    --box-bg: #f7f7f7;
    --text: #444444;
    --heading: #444444;
    --link: #0b5fa5;
    --white: #ffffff;
  }
  * { box-sizing: border-box; margin: 0; padding: 0; }
  html, body {
    width: 1200px; height: 864px; overflow: hidden;
    background: var(--page-bg);
    font-family: "Arimo", Arial, sans-serif;
    color: var(--text);
  }
  .site-frame {
    position: absolute; left: 204px; top: 54px;
    width: 781px; height: 752px;
    background: var(--frame-bg);
  }
  .masthead {
    position: absolute; left: 15px; top: 14px;
    width: 749px; height: 73px;
    background: linear-gradient(90deg, var(--brand-blue) 0%, var(--brand-blue) 55%, var(--brand-blue-deep) 80%, var(--brand-blue) 100%);
    overflow: hidden;
  }
  .masthead-texture {
    position: absolute; right: 0; top: 0; width: 340px; height: 73px;
    background: radial-gradient(ellipse at 40% 60%, rgba(0,20,60,0.35), rgba(0,20,60,0) 70%);
  }
  .journal-name {
    position: absolute; left: 20px; top: 17px;
    font-family: "Arimo", Arial, sans-serif; font-weight: 700;
    color: var(--white); font-size: 21px; line-height: 1;
  }
  .journal-tagline {
    position: absolute; left: 20px; top: 43px;
    font-family: "Arimo", Arial, sans-serif; font-weight: 400;
    color: var(--white); font-size: 14px; line-height: 1;
  }
  .main-nav {
    position: absolute; left: 15px; top: 87px;
    width: 749px; height: 35px;
    background: linear-gradient(var(--nav-top), var(--nav-bottom));
    display: flex;
  }
  .main-nav a {
    color: var(--white); text-decoration: none;
    font-size: 10.2px; font-weight: 700;
    padding: 0 9px; line-height: 35px;
    border-right: 1px solid var(--nav-divider);
  }
  .main-nav a:last-child { border-right: none; }
  .content-panel {
    position: absolute; left: 15px; top: 138px;
    width: 749px; height: 597px;
    background: var(--panel-bg);
    border: 1px solid var(--panel-border); border-radius: 3px;
  }
  .article {
    position: absolute; left: 15px; top: 36px; width: 474px;
    font-size: 11.15px; line-height: 16.4px;
  }
  .issue-cover {
    float: left; width: 159px; height: 235px;
    margin: 0 23px 16px 0;
    background: linear-gradient(160deg, #0d56a6 0%, #0a4a93 50%, #073d7e 100%);
  }
  .article-title {
    font-size: 15px; font-weight: 700; color: var(--heading);
    line-height: 1; margin: -3px 0 17px;
  }
  .article p { margin-bottom: 16.4px; }
  .sidebar {
    position: absolute; left: 503px; top: 31px; width: 228px;
  }
  .side-box {
    background: var(--box-bg);
    border: 1px solid var(--panel-border); border-radius: 3px;
    padding: 15px; margin-bottom: 16px;
    font-size: 11px; line-height: 16.4px;
  }
  .editors-box { height: 284px; padding-top: 33px; }
  .editors-box dt { font-weight: 700; }
  .editors-box dd { margin-bottom: 17px; }
  .archive-box { height: 100px; }
  .archive-box h2 { font-size: 18px; font-weight: 700; color: var(--heading); line-height: 1; margin: 1px 0 13px; }
  .archive-box ul { padding-left: 15px; }
  .archive-box a { color: var(--link); text-decoration: none; }
  .search-box { height: 57px; display: flex; gap: 3px; padding-top: 15px; }
  .search-box input {
    width: 163px; height: 24px;
    border: 1px solid #b9b9b9; background: var(--white);
  }
  .search-box button {
    width: 32px; height: 24px; font-family: inherit;
    font-size: 11px; font-weight: 700; color: #333;
    border: 1px solid #cfcfcf; border-radius: 2px;
    background: linear-gradient(#f8f8f8, #e6e6e6);
  }
</style>
</head>
<body>
  <div class="site-frame">
    <header class="masthead">
      <div class="masthead-texture" role="img" aria-label="Dark abstract smoke swirls on blue"></div>
      <div class="journal-name">The Mutable Veil</div>
      <div class="journal-tagline">Studies in Deconstruction and Psychoanalysis</div>
    </header>
    <nav class="main-nav">
      <a href="#">Issues</a>
      <a href="#">News and Events</a>
      <a href="#">Bibliography</a>
      <a href="#">Blog</a>
      <a href="#">Submissions</a>
      <a href="#">Contact</a>
      <a href="#">Links</a>
    </nav>
    <main class="content-panel">
      <article class="article">
        <div class="issue-cover" role="img" aria-label="Journal cover: blue with dark abstract swirls, title and issue number"></div>
        <h1 class="article-title">The Mutable Veil</h1>
        <p>Hendand ignatemquid quos modicipsum quae cullamendis quam, sinis int voluptati am labore cum sequi dolum ium que maxim liquia quo tem imi, si offic temporionem vollo volectium, quae sentur, ommolup tatur, sinte voluptae eumqui opta pro optur, temolor epudiam et ut apelibu storitatem quam quas aut ulparume nonserr oremporro inturestiat rerum qui consequo odipist, assundipis et, sim qui optaquam, nonsed qui si nis acietur, nonse nisquam, volupti oremquis et audit, commodis remposs itaturiam, consedia dolorum, tem res ma sendae alibus, exero int et, ut dis nihillabo.</p>
        <p>Neque si cupiene earum solorro et atincius aped magnimus qui dolupta verum quo vendigni debitam qui con ent fugia cusdae quodis alibus eat verum audandusda nis rehenim agniet alita cusapeditat et et volorecto totatistem accus ea del maxim que net venis sinimi, toribus ciunda id militem porepel itatatem estisquam estrumquaest facereicita di idusdani atur solorum fuga. Nem facimus.</p>
        <p>Hendand ignatemquid quos modicipsum quae cullamendis quam, sinis int voluptati am labore cum sequi dolum ium que maxim liquia quo tem imi, si offic temporionem vollo volectium, quae sentur, ommolup tatur, sinte voluptae eumqui opta pro optur, temolor epudiam et ut apelibu storitatem quam quas aut ulparume nonserr oremporro inturestiat rerum qui consequo odipist, assundipis et, sim qui optaquam, nonsed qui si nis acietur, nonse nisquam, volupti oremquis et audit, commodis remposs itaturiam, consedia dolorum, tem res ma sendae alibus, exero int et, ut dis nihillabo. Neque si cupiene earum solorro et atincius aped magnimus qui dolupta verum quo vendigni debitam qui con ent fugia cusdae quodis alibus eat verum audandusda nis rehenim agniet alita cusapeditat et et volorecto totatistem accus ea del maxim que net venis sinimi, toribus ciunda id militem porepel itatatem estisquam estrumquaest facereicita di idusdani atur solorum fuga. Nem facimus.</p>
      </article>
      <aside class="sidebar">
        <section class="side-box editors-box">
          <dl>
            <dt>Editor</dt>
            <dd>Owen Marsh</dd>
            <dt>Managing Editor, Founder</dt>
            <dd>Paul Dreyer</dd>
            <dt>Editorial Board</dt>
            <dd>Harold Whitcombe, Martin Fairclough, Edith Varga, Ronald Tate, Marisol Ortega Luna, Thomas Berling, Nathaniel Corrigan, Caroline Ashworth, Dylan Ferris, Ingrid Hollander, Victor Lang</dd>
          </dl>
        </section>
        <section class="side-box archive-box">
          <h2>Blog Archive</h2>
          <ul><li><a href="#">December 2013</a> (2)</li></ul>
        </section>
        <form class="side-box search-box">
          <input type="text" aria-label="Search">
          <button type="button">Go</button>
        </form>
      </aside>
    </main>
  </div>
</body>
</html>
```